Visual consulting framework

Tamsworth Advisory is a financial consulting business that takes it clients on the following journey:
1. Get fit (disciplined)
2. Get funded (access to capital)
3. Get big (grow)
4. Get out (exit with wealth)
Over thirty years we have identified that the key to being successful on this journey are the following elements or components.
1. Vision
2. Strategy
3. Structure
4. Product & services
5. Sales and marketing
6. System and processes
7. People
8. Culture
9. Finance
10. M&A
11. Performance monitoring
12. Risk management
We require a visual representation of these elements and the journey to communicate to clients and prospects in marketing material.

```html
<!DOCTYPE html>
<html lang="en">
<head>
<meta charset="UTF-8">
<title>Tamsworth Advisory – Consulting Framework</title>
<link href="https://fonts.googleapis.com/css2?family=Poppins:wght@400;600&family=Lato:wght@400&display=swap" rel="stylesheet">
<style>
  :root {
    --night: #05070c;
    --night-blue: #16202e;
    --pink: #ec3c8e;
    --pink-deep: #b9339a;
    --orange: #f9a01b;
    --orange-deep: #f7931e;
    --yellow: #fdc12a;
    --blue: #35c3ef;
    --blue-deep: #139fd8;
    --green: #2fd88a;
    --green-deep: #19b36a;
    --card: #f4f4f4;
    --label: #6d6d6d;
    --hub: #ece3e3;
    --hub-text: #8a8a8a;
    --hub-icon: #b5b5b5;
  }
  * { margin: 0; padding: 0; box-sizing: border-box; }
  html, body { width: 1200px; height: 1200px; overflow: hidden; background: var(--night); }
  .poster { position: relative; width: 1200px; height: 1200px; font-family: "Poppins", sans-serif; }
  .earth-backdrop {
    position: absolute; inset: 0;
    background:
      radial-gradient(ellipse 900px 500px at 30% 80%, rgba(120, 90, 40, 0.35), transparent 70%),
      radial-gradient(ellipse 700px 400px at 85% 75%, rgba(110, 85, 40, 0.3), transparent 70%),
      linear-gradient(175deg, var(--night) 0%, var(--night) 30%, var(--night-blue) 60%, #1b2532 100%);
  }
  .brand {
    position: absolute; left: 800px; top: 48px;
    display: flex; align-items: center; gap: 18px;
  }
  .brand-dot { width: 70px; height: 70px; border-radius: 50%; background: var(--orange-deep); }
  .brand-name {
    color: var(--orange-deep); font-weight: 400; font-size: 34px; line-height: 1.05;
    letter-spacing: 2px; text-transform: uppercase;
  }
  .stage-title {
    position: absolute; width: 420px; text-align: center;
    font-weight: 600; font-size: 48px; letter-spacing: 0.5px;
  }
  .title-fit { left: 194px; top: 200px; color: var(--pink); }
  .title-funded { left: 584px; top: 200px; color: var(--orange); }
  .title-big { left: 194px; top: 1050px; color: var(--blue); }
  .title-out { left: 584px; top: 1050px; color: var(--green-deep); }

  .stage-card { position: absolute; width: 370px; height: 370px; border-radius: 60px; padding: 16px; }
  .card-fit { left: 219px; top: 275px; background: linear-gradient(135deg, var(--pink) 30%, var(--pink-deep)); }
  .card-funded { left: 609px; top: 275px; background: linear-gradient(135deg, var(--yellow), var(--orange-deep)); }
  .card-big { left: 219px; top: 660px; background: linear-gradient(135deg, var(--blue) 30%, var(--blue-deep)); }
  .card-out { left: 609px; top: 660px; background: linear-gradient(135deg, var(--green-deep), var(--green) 60%); }
  .card-face {
    position: relative; width: 100%; height: 100%; border-radius: 46px;
    background: linear-gradient(135deg, #efefef, #fbfbfb);
  }
  .element-list {
    position: absolute; left: 0; right: 0; list-style: none; text-align: center;
    color: var(--label); font-size: 22px; letter-spacing: 0.5px; line-height: 38.5px;
  }
  .card-fit .element-list, .card-funded .element-list { top: 81px; }
  .card-big .element-list, .card-out .element-list { top: 97px; line-height: 45px; }
  .card-out .element-list { font-size: 18.5px; }
  .stage-icon { position: absolute; }

  .purpose-hub {
    position: absolute; left: 455px; top: 506px; width: 292px; height: 292px; border-radius: 50%;
    background: radial-gradient(circle at 50% 35%, #efe7e7, var(--hub) 70%, #e2d6d6);
    border: 6px solid #f6f1f1;
    box-shadow: 0 20px 60px rgba(90, 50, 50, 0.35), 0 0 40px rgba(255, 255, 255, 0.15);
    text-align: center;
  }
  .hub-icon { position: absolute; left: 103px; top: 72px; }
  .purpose-text {
    position: absolute; left: 40px; right: 40px; top: 190px;
    font-family: "Lato", sans-serif; font-size: 12px; line-height: 17px; color: var(--hub-text);
  }
</style>
</head>
<body>
<div class="poster">
  <div class="earth-backdrop" role="img" aria-label="Night view of Earth from space with glowing city lights"></div>

  <div class="brand">
    <span class="brand-dot"></span>
    <span class="brand-name">Tamsworth<br>Advisory</span>
  </div>

  <h2 class="stage-title title-fit">GET FIT</h2>
  <h2 class="stage-title title-funded">GET FUNDED</h2>

  <div class="stage-card card-fit">
    <div class="card-face">
      <ul class="element-list"><li>PRODUCT &amp; SERVICES</li><li>STRATEGY</li><li>STRUCTURE</li></ul>
      <svg class="stage-icon" style="left:142px;top:244px" width="76" height="64" viewBox="0 0 76 64">
        <path d="M3 21 H40 V3 L72 32 L40 61 V43 H3 Z" fill="none" stroke="#ec3c8e" stroke-width="4" stroke-linejoin="round"/>
      </svg>
    </div>
  </div>

  <div class="stage-card card-funded">
    <div class="card-face">
      <ul class="element-list"><li>PEOPLE</li><li>SALES AND MARKETING</li><li>SYSTEM AND PROCESSES</li></ul>
      <svg class="stage-icon" style="left:135px;top:236px" width="100" height="66" viewBox="0 0 100 66">
        <g fill="#f9a01b" stroke="#f4f4f4" stroke-width="2">
          <ellipse cx="80" cy="50" rx="18" ry="6"/><ellipse cx="80" cy="42" rx="18" ry="6"/>
          <ellipse cx="80" cy="34" rx="18" ry="6"/><ellipse cx="80" cy="26" rx="18" ry="6"/>
          <ellipse cx="18" cy="38" rx="14" ry="5"/><ellipse cx="18" cy="30" rx="14" ry="5"/>
          <ellipse cx="18" cy="22" rx="14" ry="5"/><ellipse cx="18" cy="14" rx="14" ry="5"/>
          <ellipse cx="46" cy="54" rx="26" ry="8"/><ellipse cx="46" cy="45" rx="26" ry="8"/>
          <ellipse cx="46" cy="36" rx="26" ry="8"/><ellipse cx="46" cy="27" rx="26" ry="8"/>
          <ellipse cx="46" cy="18" rx="26" ry="8"/><ellipse cx="46" cy="9" rx="26" ry="8"/>
        </g>
        <path d="M2 56 H16 M10 62 H40 M56 62 H80 M84 56 H96" stroke="#f9a01b" stroke-width="2"/>
      </svg>
    </div>
  </div>

  <div class="stage-card card-big">
    <div class="card-face">
      <ul class="element-list"><li>CULTURE</li><li>FINANCE</li><li>M&amp;A</li></ul>
      <svg class="stage-icon" style="left:152px;top:260px" width="64" height="58" viewBox="0 0 64 58">
        <g fill="#35c3ef">
          <rect x="2" y="34" width="10" height="24"/><rect x="16" y="30" width="10" height="28"/>
          <rect x="30" y="26" width="10" height="32"/><rect x="44" y="20" width="10" height="38"/>
          <path d="M0 28 C16 18 30 14 44 12 L40 4 L62 0 L58 22 L52 16 C36 20 20 26 0 36 Z"/>
        </g>
      </svg>
    </div>
  </div>

  <div class="stage-card card-out">
    <div class="card-face">
      <ul class="element-list"><li>VISION</li><li>RISK MANAGEMENT</li><li>PERFORMANCE MONITORING</li></ul>
      <svg class="stage-icon" style="left:138px;top:254px" width="76" height="64" viewBox="0 0 76 64">
        <path d="M3 21 H40 V3 L72 32 L40 61 V43 H3 Z" fill="none" stroke="#19b36a" stroke-width="4" stroke-linejoin="round"/>
      </svg>
    </div>
  </div>

  <div class="purpose-hub">
    <svg class="hub-icon" width="74" height="74" viewBox="0 0 74 74">
      <circle cx="37" cy="37" r="34" fill="#b5b5b5"/>
      <path d="M21 38 L32 49 L53 26" fill="none" stroke="#f3ecec" stroke-width="7" stroke-linecap="round" stroke-linejoin="round"/>
    </svg>
    <p class="purpose-text">Our purpose is clear, we get companies and their founders, fit, funded, big and out</p>
  </div>

  <h2 class="stage-title title-big">GET BIG</h2>
  <h2 class="stage-title title-out">GET OUT</h2>
</div>
</body>
</html>
```